Info Graphic Poster Needed

We need a poster illustrating how to put on Cryo gear. Instructions with some graphics next to them that are good examples of what to do..etc.
" How to put on gear for Cyro treatment
1. Remove clothing down to underwear or workout clothes
2. Socks and slippers
3. Facemask
4. Ear warmers
5. Gloves
6. Mittens
7. Wrap towel/robe over chest for women and over bottom for men if desired
8. Request robe if desired "
We would like our logo on the bottom of the poster (logo attached)
We like very modern designs.
Thank you!!

```html
<!DOCTYPE html>
<html lang="en">
<head>
<meta charset="utf-8">
<title>How to Wear Your Cryo Gear</title>
<link href="https://fonts.googleapis.com/css2?family=Roboto+Condensed:wght@400;700&family=Roboto:wght@400;700&display=swap" rel="stylesheet">
<style>
  :root {
    --ink: #5f6163;
    --hex-fill: #39c3ef;
    --hex-line: #1d3440;
    --badge: #2197c4;
    --badge-text: #e9f7fc;
    --bg-light: #f1fbfe;
    --bg-mid: #c9eff9;
    --bg-soft: #dff6fc;
    --bg-edge: #8fdcf1;
    --brand: #1f4f9a;
  }
  * { box-sizing: border-box; margin: 0; padding: 0; }
  html, body { width: 1004px; height: 1200px; overflow: hidden; }
  body { background: #ffffff; font-family: "Roboto", Arial, sans-serif; color: var(--ink); }

  .poster {
    position: relative;
    width: 1004px;
    height: 1200px;
    overflow: hidden;
  }
  .poster-backdrop {
    position: absolute; inset: 0;
    background:
      radial-gradient(ellipse 50% 40% at 50% 48%, var(--bg-light) 0%, rgba(241,251,254,0) 100%),
      linear-gradient(60deg, rgba(255,255,255,0) 0%, rgba(255,255,255,0.35) 25%, rgba(255,255,255,0) 50%, rgba(255,255,255,0.3) 75%, rgba(255,255,255,0) 100%),
      linear-gradient(135deg, var(--bg-edge) 0%, var(--bg-mid) 22%, var(--bg-soft) 50%, var(--bg-mid) 78%, var(--bg-edge) 100%);
  }

  .centered { position: absolute; transform: translate(-50%, -50%); white-space: nowrap; text-align: center; }

  .poster-title {
    left: 502px; top: 56px;
    font-family: "Roboto Condensed", Arial, sans-serif;
    font-weight: 700; font-size: 46px; letter-spacing: 0.5px;
  }
  .attire-heading {
    left: 502px; top: 108px;
    font-weight: 700; font-size: 18px; letter-spacing: 0.4px;
  }
  .attire-line {
    font-family: "Roboto Condensed", Arial, sans-serif;
    font-size: 18px; left: 490px;
  }
  .attire-line.first { top: 131px; }
  .attire-line.second { top: 153px; }

  .defs { position: absolute; width: 0; height: 0; }

  .hex { position: absolute; width: 258px; height: 194px; transform: translate(-50%, -50%); }
  .hex .hex-shape { fill: var(--hex-fill); stroke: var(--hex-line); stroke-width: 1.5; }
  .hex .art-area { fill: url(#artTone); }

  .step-badge {
    position: absolute; width: 58px; height: 58px; border-radius: 50%;
    transform: translate(-50%, -50%);
    background: var(--badge); border: 1.5px solid var(--hex-line);
    color: var(--badge-text);
    font-weight: 700; font-size: 34px; line-height: 55px; text-align: center;
  }

  .gear-label {
    font-family: "Roboto Condensed", Arial, sans-serif;
    font-weight: 700; font-size: 19px;
  }

  .center-word {
    left: 503px;
    font-family: "Roboto", Arial, sans-serif;
    font-weight: 700; font-size: 76px; letter-spacing: 1px;
  }
  .center-word.top { top: 491px; }
  .center-word.bottom { top: 578px; }

  .rule-note {
    position: absolute; top: 937px; transform: translateY(-50%);
    font-weight: 700; font-size: 20px; white-space: nowrap;
    display: flex; align-items: center; gap: 10px;
  }
  .rule-note::before {
    content: ""; width: 11px; height: 11px; border-radius: 50%; background: var(--ink);
  }
  .rule-note.dry { left: 58px; }
  .rule-note.phones { left: 570px; }

  .closing-line {
    left: 503px; top: 1015px;
    font-family: "Roboto Condensed", Arial, sans-serif;
    font-weight: 700; font-size: 40px;
  }

  .brand-name {
    position: absolute; left: 26px; top: 1120px; transform: translateY(-50%);
    font-family: "Roboto", Arial, sans-serif; font-weight: 400;
    font-size: 50px; letter-spacing: 2px; color: var(--brand);
  }
</style>
</head>
<body>
<main class="poster">
  <div class="poster-backdrop" role="img" aria-label="Faceted icy blue triangle pattern background"></div>

  <svg class="defs" aria-hidden="true">
    <defs>
      <radialGradient id="artTone" cx="50%" cy="50%" r="50%">
        <stop offset="0%" stop-color="#e4e8eb"/>
        <stop offset="45%" stop-color="#b7c3ca"/>
        <stop offset="100%" stop-color="#39c3ef" stop-opacity="0"/>
      </radialGradient>
    </defs>
  </svg>

  <h1 class="centered poster-title">HOW TO WEAR YOUR CRYO GEAR</h1>
  <p class="centered attire-heading">EXAMPLES OF APPROPRIATE ATTIRE:</p>
  <p class="centered attire-line first">DRY WORKOUT CLOTHES OR</p>
  <p class="centered attire-line second">UNDER GARMENTS</p>

  <svg class="hex" style="left:495px;top:268px" viewBox="0 0 258 194" role="img" aria-label="Illustration: man and woman in dark workout shorts and tops">
    <polygon class="hex-shape" points="1,97 58,1 200,1 257,97 200,193 58,193"/>
    <ellipse class="art-area" cx="129" cy="97" rx="80" ry="88"/>
  </svg>
  <svg class="hex" style="left:721px;top:368px" viewBox="0 0 258 194" role="img" aria-label="Illustration: feet in tall socks and slippers">
    <polygon class="hex-shape" points="1,97 58,1 200,1 257,97 200,193 58,193"/>
    <ellipse class="art-area" cx="129" cy="97" rx="100" ry="70"/>
  </svg>
  <svg class="hex" style="left:808px;top:573px" viewBox="0 0 258 194" role="img" aria-label="Illustration: two people wearing black face masks">
    <polygon class="hex-shape" points="1,97 58,1 200,1 257,97 200,193 58,193"/>
    <ellipse class="art-area" cx="135" cy="110" rx="105" ry="70"/>
  </svg>
  <svg class="hex" style="left:653px;top:763px" viewBox="0 0 258 194" role="img" aria-label="Illustration: side profile of a person wearing an ear warmer">
    <polygon class="hex-shape" points="1,97 58,1 200,1 257,97 200,193 58,193"/>
    <ellipse class="art-area" cx="135" cy="100" rx="70" ry="92"/>
  </svg>
  <svg class="hex" style="left:358px;top:763px" viewBox="0 0 258 194" role="img" aria-label="Illustration: pair of white gloves">
    <polygon class="hex-shape" points="1,97 58,1 200,1 257,97 200,193 58,193"/>
    <ellipse class="art-area" cx="125" cy="105" rx="80" ry="88"/>
  </svg>
  <svg class="hex" style="left:201px;top:573px" viewBox="0 0 258 194" role="img" aria-label="Illustration: pair of grey knitted mittens">
    <polygon class="hex-shape" points="1,97 58,1 200,1 257,97 200,193 58,193"/>
    <ellipse class="art-area" cx="110" cy="100" rx="95" ry="82"/>
  </svg>
  <svg class="hex" style="left:274px;top:368px" viewBox="0 0 258 194" role="img" aria-label="Illustration: man and woman wrapped in towels wearing full cryo gear">
    <polygon class="hex-shape" points="1,97 58,1 200,1 257,97 200,193 58,193"/>
    <ellipse class="art-area" cx="120" cy="97" rx="80" ry="90"/>
  </svg>

  <div class="step-badge" style="left:498px;top:371px">1</div>
  <div class="step-badge" style="left:625px;top:412px">2</div>
  <div class="step-badge" style="left:682px;top:562px">3</div>
  <div class="step-badge" style="left:595px;top:671px">4</div>
  <div class="step-badge" style="left:420px;top:671px">5</div>
  <div class="step-badge" style="left:327px;top:562px">6</div>
  <div class="step-badge" style="left:366px;top:414px">7</div>

  <span class="centered gear-label" style="left:273px;top:249px">TOWEL WRAP</span>
  <span class="centered gear-label" style="left:746px;top:255px">SOCKS AND SLIPPERS</span>
  <span class="centered gear-label" style="left:134px;top:457px">MITTENS</span>
  <span class="centered gear-label" style="left:870px;top:457px">FACEMASK</span>
  <span class="centered gear-label" style="left:358px;top:888px">GLOVES</span>
  <span class="centered gear-label" style="left:667px;top:888px">EAR WARMERS OR BEANIE</span>

  <p class="centered center-word top">CRYO</p>
  <p class="centered center-word bottom">GEAR</p>

  <p class="rule-note dry">ALL ATTIRE AND HAIR MUST BE DRY</p>
  <p class="rule-note phones">NO PHONES IN THE CHAMBER</p>

  <p class="centered closing-line">CONGRATULATIONS YOU ARE NOW A CRYO NINJA!</p>

  <p class="brand-name">CLEARPEAK</p>
</main>
</body>
</html>
```